Book Cover Design Project

A non-fiction book on child protection, specifically... keeping young children safe from predators and keeping teenagers safe from themselves.

Title:
Under Our Roof

Subtitle:
A Guide To Keeping Your Children Safe

Author:
Martin Kellerby

```html
<!DOCTYPE html>
<html lang="en">
<head>
<meta charset="utf-8">
<title>Under Our Roof — Book Cover</title>
<link rel="stylesheet" href="https://fonts.googleapis.com/css2?family=Archivo+Black&family=Oswald:wght@600&display=swap">
<style>
  :root {
    --paper: #ffffff;
    --ink: #111111;
    --band: #bdbdbd;
    --photo-light: #d9d6d2;
    --photo-mid: #a9a39c;
    --photo-dark: #5a4e46;
  }
  html, body {
    margin: 0;
    padding: 0;
    overflow: hidden;
    background: var(--paper);
  }
  .cover {
    position: relative;
    width: 916px;
    height: 1200px;
    background: var(--paper);
    overflow: hidden;
  }
  .spine-band {
    position: absolute;
    left: 0;
    top: 0;
    width: 198px;
    height: 1200px;
    background: var(--band);
  }
  .vertical-title {
    position: absolute;
    left: 0;
    top: 0;
    width: 916px;
    height: 1200px;
  }
  .vertical-title text {
    font-family: "Archivo Black", "Arial Black", sans-serif;
    font-size: 262px;
  }
  .subtitle {
    position: absolute;
    left: 251px;
    top: 52px;
    margin: 0;
    font-family: "Oswald", "Arial Narrow", sans-serif;
    font-weight: 600;
    font-size: 41px;
    line-height: 66px;
    color: var(--ink);
    letter-spacing: -0.3px;
  }
  .subtitle span { display: block; }
  .author {
    position: absolute;
    right: 10px;
    top: 210px;
    margin: 0;
    font-family: "Oswald", "Arial Narrow", sans-serif;
    font-weight: 600;
    font-size: 33px;
    color: var(--ink);
  }
  .cover-photo {
    position: absolute;
    left: 251px;
    top: 982px;
    width: 660px;
    height: 206px;
    background: linear-gradient(180deg, var(--photo-light) 0%, var(--photo-mid) 55%, var(--photo-light) 100%);
  }
  .cover-photo::after {
    content: "";
    position: absolute;
    left: 30px;
    right: 60px;
    top: 50px;
    bottom: 45px;
    border-radius: 60px;
    background: var(--photo-dark);
    opacity: 0.55;
  }
</style>
</head>
<body>
<main class="cover">
  <div class="spine-band"></div>

  <svg class="vertical-title" viewBox="0 0 916 1200" aria-label="Under Our Roof">
    <defs>
      <clipPath id="on-band"><rect x="0" y="0" width="198" height="1200"/></clipPath>
      <clipPath id="off-band"><rect x="198" y="0" width="718" height="1200"/></clipPath>
    </defs>
    <g clip-path="url(#on-band)">
      <text transform="translate(226 1190) rotate(-90)" fill="var(--paper)" textLength="1150" lengthAdjust="spacingAndGlyphs">Under Our Roof</text>
    </g>
    <g clip-path="url(#off-band)">
      <text transform="translate(226 1190) rotate(-90)" fill="var(--ink)" textLength="1150" lengthAdjust="spacingAndGlyphs">Under Our Roof</text>
    </g>
  </svg>

  <h2 class="subtitle">
    <span>A Guide</span>
    <span>To Keeping Your Children Safe</span>
  </h2>

  <p class="author">Martin Kellerby</p>

  <div class="cover-photo" role="img" aria-label="Photograph of a young child lying asleep on a paved street"></div>
</main>
</body>
</html>
```